VelunaBay Spa, Skincare and Cosmetics website

I need a website for VelunaBay (putting the glow back into people's skin) which allows viewers to access information about Beauty Spa packaging and facilities as well as online skincare and cosmetic products. Our distinctive difference is that our products are certified organic. We want to target a luxury high income niche market (age 30-50). I want all colours to be "baby colours" preferably background to be "baby metallic pink" (but please don't make the website too immature) with curves as patterns. I want a romantic vintage look.

The website needs to look:
1. elegant (prestige and luxury)
2. bright (baby colours mainly)
3. European curves and signature patterns
4. Can include Pearl related pics (but not a must)

The website pages needs to have:
1. pages ordering skincare/cosmetics
2. shopping cart and payment
3. about us and about our product differences
4. contact us
5. booking for spa treatments and packages

I have attached our logo and also packaging label styles.

```html
<!DOCTYPE html>
<html lang="en">
<head>
<meta charset="utf-8">
<title>VelunaBay Spa, Skincare and Cosmetics</title>
<link href="https://fonts.googleapis.com/css2?family=Playfair+Display:ital,wght@0,400;0,700;1,400&family=Raleway:wght@400;500;600;700&family=Open+Sans:wght@400;600;700&family=Great+Vibes&display=swap" rel="stylesheet">
<style>
:root{
  --blush:#f7e9e3;
  --blush-deep:#ecd4c9;
  --paper:#fdf8f6;
  --cocoa:#4a2414;
  --cocoa-dark:#2b140b;
  --rust:#8d2f10;
  --ink:#3a2e2a;
  --muted:#8a7b75;
  --night:#1c1513;
  --line:#dcc6bc;
  --white:#ffffff;
  --peach:#ffb48a;
}
*{box-sizing:border-box;margin:0;padding:0}
html,body{width:1200px;height:4836px;overflow:hidden}
body{background:var(--blush);font-family:"Open Sans",Arial,sans-serif;color:var(--ink);font-size:15px;line-height:1.6}
.wrap{width:1040px;margin:0 auto;position:relative;height:100%}
.ph{display:block}
h2.section-title{font-family:"Raleway",Arial,sans-serif;text-align:center;color:var(--ink)}
.kicker{display:block;font-family:"Raleway",Arial,sans-serif;font-size:22px;color:var(--muted);text-align:center}
.big{font-size:52px;font-weight:700;line-height:1.1;letter-spacing:1px}

/* hero */
.hero{height:800px;position:relative;overflow:hidden;
  background:
    radial-gradient(ellipse 380px 260px at 700px 260px,#e9c9b2 0%,rgba(233,201,178,0) 100%),
    radial-gradient(ellipse 300px 200px at 1000px 420px,#7a4a32 0%,rgba(122,74,50,0) 100%),
    radial-gradient(ellipse 220px 300px at 150px 520px,#3a2218 0%,rgba(58,34,24,0) 100%),
    linear-gradient(100deg,#5a3828 0%,#9c7560 25%,#cfae97 48%,#b78d74 68%,#6e4430 100%)}
.hero-top{position:absolute;top:0;left:0;right:0;height:120px;background:rgba(43,20,11,.6)}
.brand{position:absolute;left:110px;top:34px;display:flex;align-items:center;gap:12px;font-family:"Playfair Display",serif;font-size:34px;color:var(--white)}
.brand-dot{width:26px;height:26px;border-radius:50%;background:var(--white)}
.util{position:absolute;right:90px;top:10px;display:flex;gap:24px;font-size:13px;color:#e8d8d0}
.nav{position:absolute;right:90px;top:58px;display:flex;gap:44px;font-family:"Raleway",sans-serif;font-size:17px;font-weight:600;color:var(--white)}
.hero-copy{position:absolute;left:470px;top:500px;width:700px;text-align:center;color:var(--white)}
.hero-copy h1{font-family:"Playfair Display",serif;font-weight:700;font-size:50px;line-height:1.15;background:rgba(43,20,11,.55);padding:10px 20px 12px;text-shadow:0 2px 6px rgba(0,0,0,.35)}
.hero-copy h1 em{font-style:normal;color:var(--peach)}
.hero-band{margin:0 auto;width:640px;background:rgba(255,255,255,.3);padding:10px 20px 14px}
.hero-band .tag{font-family:"Playfair Display",serif;font-style:italic;font-size:44px;color:var(--white);text-shadow:0 2px 6px rgba(0,0,0,.3)}
.hero-band p{font-size:13px;color:#fff;text-shadow:0 1px 3px rgba(0,0,0,.4)}

.slide-bar{height:60px;background:var(--cocoa-dark);display:flex;align-items:center;padding:0 30px;color:#e8d8d0}
.slide-bar .ctrl{display:flex;gap:10px;align-items:center}
.circ{width:32px;height:32px;border-radius:50%;background:#efe4de;display:flex;align-items:center;justify-content:center}
.dots{display:flex;gap:8px;margin-left:22px}
.dots i{width:10px;height:10px;border-radius:50%;background:#d9c8c0;display:block}
.support{margin-left:auto;display:flex;align-items:center;gap:10px;font-size:12px;line-height:1.3}
.support b{display:block;font-size:13px;color:var(--white)}
.social{display:flex;gap:10px;margin-left:40px}
.social i{width:22px;height:22px;border-radius:50%;background:#7a5a4c;display:block}

/* intro */
.intro{height:300px;background:var(--paper)}
.intro .lead{position:absolute;left:0;top:40px;width:620px}
.intro small{font-size:14px;color:var(--muted)}
.intro h3{font-family:"Playfair Display",serif;font-size:34px;font-weight:400;color:var(--ink);margin:4px 0 10px}
.intro .lead p{font-size:13px;color:var(--muted)}
.intro .rule{position:absolute;left:650px;top:40px;width:1px;height:200px;background:var(--line)}
.intro .avatar{position:absolute;left:690px;top:50px;width:110px;height:110px;border-radius:50%;background:radial-gradient(circle at 40% 35%,#e6c7b5,#8f6a58)}
.intro blockquote{position:absolute;left:820px;top:40px;width:230px;font-family:"Playfair Display",serif;font-style:italic;font-size:17px;color:var(--ink);line-height:1.5}
.signature{position:absolute;left:820px;top:210px;font-family:"Great Vibes",cursive;font-size:34px;color:var(--rust)}

/* what's new */
.whats{height:680px}
.whats .heading{position:absolute;top:40px;left:0;right:0}
.whats .underline{width:1040px;height:1px;background:var(--line);margin:14px auto 0}
.latest{position:absolute;left:0;top:180px;width:240px;height:200px;background:var(--white);padding:26px 22px}
.latest h4{font-family:"Raleway",sans-serif;font-size:22px;font-weight:700}
.latest p{font-size:12px;color:var(--muted);margin-top:6px}
.latest .pager{position:absolute;bottom:18px;left:22px;display:flex;gap:8px;align-items:center}
.pager i{width:8px;height:8px;border-radius:50%;background:var(--line);display:block}
.tile{position:absolute;top:180px;width:240px;height:200px}
.feature{position:absolute;left:780px;top:180px;width:260px;height:460px;background:linear-gradient(180deg,#c8a48d,#8a5f48 70%,#5e3a28)}
.feature .cap-top{position:absolute;top:16px;left:16px;font-family:"Raleway",sans-serif;font-size:26px;color:var(--white)}
.feature .cap-bot{position:absolute;bottom:0;left:0;right:0;background:rgba(43,20,11,.6);padding:16px;color:var(--white);font-family:"Raleway",sans-serif;font-size:20px;line-height:1.3}
.news{position:absolute;left:0;top:400px;width:760px}
.news-row{display:flex;gap:16px;height:80px;border-bottom:1px solid var(--line);padding:8px 0}
.news-row .thumb{width:86px;height:62px;background:linear-gradient(135deg,#e6c3b2,#b07c66)}
.news-row .body{flex:1}
.news-row .meta{display:flex;justify-content:space-between;font-size:13px}
.news-row .meta b{color:var(--rust);font-weight:700}
.news-row p{font-size:11px;color:var(--muted);line-height:1.45}

/* heart it */
.heart{height:600px;background:var(--paper)}
.heart .heading{position:absolute;top:50px;left:0;right:0}
.cards{position:absolute;top:180px;left:0;display:flex;gap:20px}
.card{width:245px;background:var(--white);box-shadow:0 3px 8px rgba(74,36,20,.12)}
.card .img{height:290px}
.price{height:44px;background:var(--cocoa-dark);color:var(--white);text-align:center;font-weight:700;line-height:44px}
.icons{height:46px;display:flex;justify-content:space-around;align-items:center}

/* experts */
.experts{height:580px;background:var(--blush-deep)}
.experts .heading{position:absolute;top:40px;left:0;right:0}
.expert-card{position:absolute;top:160px;left:0;width:1040px;height:380px;background:var(--white);display:flex}
.expert-card .img{width:540px;height:380px;background:linear-gradient(120deg,#5b3424,#a97b62 55%,#e7cfc2)}
.expert-card .txt{padding:60px 40px;width:430px}
.expert-card h4{font-family:"Raleway",sans-serif;font-size:30px;font-weight:500;line-height:1.15}
.expert-card p{font-size:12px;color:var(--muted);margin:16px 0 22px}
.btn{display:inline-block;background:var(--cocoa-dark);color:var(--white);font-size:11px;font-weight:700;padding:8px 16px}
.expert-card .next{position:absolute;right:30px;top:170px}

/* testimonials */
.testi{height:640px;background:var(--paper)}
.testi .heading{position:absolute;top:40px;left:0;right:0}
.testi .heading h2{font-size:40px;font-weight:600}
.testi .heading span{display:block;text-align:center;font-size:19px;color:var(--muted);font-family:"Raleway",sans-serif}
.quote{position:absolute;top:170px;left:0;width:1040px;height:190px;background:#e6dcd8;padding:30px 50px}
.quote .mark{position:absolute;left:16px;top:10px;font-family:"Playfair Display",serif;font-size:52px;color:var(--ink)}
.quote p{font-size:14px;color:var(--muted)}
.quote .who{position:absolute;right:30px;bottom:14px;font-size:13px;color:var(--rust);font-weight:700}
.faces{position:absolute;top:380px;left:0;width:1040px;display:flex;justify-content:space-between;align-items:center}
.faces div{width:96px;height:110px;background:linear-gradient(180deg,#d8c3b8,#9a8178)}
.faces .on{width:118px;height:140px;background:linear-gradient(180deg,#c99e87,#6e4a3a)}

/* products */
.products{height:510px}
.products .heading{position:absolute;top:30px;left:0;right:0}
.products .heading h2{font-size:40px;font-weight:600}
.products .heading span{display:block;text-align:center;font-size:20px;color:var(--muted);font-family:"Raleway",sans-serif}
.tabs{position:absolute;top:150px;left:240px;display:flex;gap:26px;font-family:"Raleway",sans-serif;font-size:18px;align-items:center}
.tabs .active{background:var(--rust);color:var(--white);padding:2px 14px}
.tabs-line{position:absolute;top:182px;left:0;width:1040px;height:2px;background:var(--rust)}
.shelf{position:absolute;top:200px;left:0;display:flex;gap:20px}
.item{width:245px;height:240px;background:var(--white);padding:14px;position:relative}
.item h5{font-family:"Raleway",sans-serif;font-size:18px;font-weight:700}
.item small{font-size:11px;color:var(--muted)}
.item .pic{position:absolute;left:50%;bottom:16px;width:90px;height:130px;transform:translateX(-50%)}

/* newsletter */
.newsletter{height:120px;background:var(--cocoa)}
.newsletter .wrap{display:flex}
.newsletter .half{width:520px;padding:20px 0}
.newsletter h4{font-family:"Raleway",sans-serif;color:var(--white);font-size:20px;font-weight:700}
.signup{display:flex;margin-top:14px}
.signup span{width:380px;height:34px;background:var(--white)}
.signup b{background:var(--cocoa-dark);color:var(--white);font-size:13px;padding:6px 16px}
.newsletter p{font-size:12px;color:#e1c6b9;line-height:1.5;margin-top:8px}

/* footer */
.footer{height:470px;background:var(--night);color:#b9aaa3}
.mag{position:absolute;left:0;top:30px;width:200px;height:270px;background:linear-gradient(160deg,#e8d7cf,#a88170 60%,#3e2820)}
.footer h4{font-family:"Raleway",sans-serif;font-size:20px;color:var(--white);font-weight:600;margin-bottom:10px}
.footer p{font-size:11px;line-height:1.6}
.col{position:absolute}
.salon-pic{width:100px;height:70px;background:linear-gradient(135deg,#8c6757,#3d2a22);float:left;margin-right:12px}
.hours div{display:flex;justify-content:space-between;font-size:11px;border-bottom:1px solid #2f2623;padding:3px 0}
.contact p{margin-bottom:4px}
.bottom{height:76px;background:var(--night);border-top:1px solid #2f2623}
.bottom .wrap{display:flex;align-items:center}
.pay{display:flex;gap:10px}
.pay i{display:block;width:44px;height:26px;background:#3b302c}
.copy{margin-left:auto;font-size:12px;color:#8e7f79}
</style>
</head>
<body>

<header class="hero">
  <div class="ph" role="img" aria-label="Photo of a woman relaxing during a spa treatment with candles and bath salts" style="position:absolute;inset:0"></div>
  <div class="hero-top"></div>
  <div class="brand"><span class="brand-dot"></span>VelunaBay</div>
  <div class="util"><span>Account</span><span>Login</span><span>Register</span><span>Checkout</span></div>
  <nav class="nav"><span>Home</span><span>Spa &amp; Treatments</span><span>Products</span><span>Booking</span><span>Blog</span><span>Contact</span></nav>
  <div class="hero-copy">
    <h1>An exhaustive resource of<br><em>spa treatments.</em></h1>
    <div class="hero-band">
      <div class="tag">Simple, Fast &amp; Secure</div>
      <p>Book organic rituals, skincare and cosmetics in one calm place, crafted for your glow.</p>
    </div>
  </div>
</header>

<div class="slide-bar">
  <div class="ctrl">
    <span class="circ"><svg width="12" height="12" viewBox="0 0 12 12"><path d="M8 1 3 6l5 5" stroke="#4a2414" stroke-width="2" fill="none"/></svg></span>
    <span class="circ"><svg width="12" height="12" viewBox="0 0 12 12"><path d="M4 1l5 5-5 5" stroke="#4a2414" stroke-width="2" fill="none"/></svg></span>
    <div class="dots"><i></i><i></i><i></i><i></i></div>
  </div>
  <div class="support">
    <svg width="22" height="22" viewBox="0 0 24 24"><path d="M6 3h4l2 5-3 2a11 11 0 0 0 5 5l2-3 5 2v4a2 2 0 0 1-2 2A17 17 0 0 1 4 5a2 2 0 0 1 2-2z" fill="#e8d8d0"/></svg>
    <div><b>CUSTOMER SUPPORT</b>+1 (555) 014-2290</div>
  </div>
  <div class="social"><i></i><i></i><i></i><i></i><i></i><i></i></div>
</div>

<section class="intro">
  <div class="wrap">
    <div class="lead">
      <small>Exclusively For You From Her Salon</small>
      <h3>A Brand New Way to Experience Beauty</h3>
      <p>Our certified organic rituals blend gentle botanicals with expert hands. Every treatment is tailored to restore calm, balance and a natural radiance. Discover facials, massages and bespoke packages designed for the modern woman who values quiet luxury and time well spent.</p>
    </div>
    <div class="rule"></div>
    <div class="avatar" role="img" aria-label="Portrait of the salon founder"></div>
    <blockquote>Over the last eighteen months our salon has increased three-fold since the launch of our new web site.</blockquote>
    <div class="signature">Camille Arden</div>
  </div>
</section>

<section class="whats">
  <div class="wrap">
    <div class="heading">
      <span class="kicker">New in July 2013</span>
      <h2 class="section-title big">Whats New.</h2>
      <div class="underline"></div>
    </div>
    <div class="latest">
      <h4>Our latest projects</h4>
      <p>Fresh rituals and seasonal treatments now open for booking.</p>
      <div class="pager">
        <svg width="10" height="10"><path d="M7 1 3 5l4 4" stroke="#8a7b75" fill="none" stroke-width="1.5"/></svg>
        <i></i><i></i><i></i>
        <svg width="10" height="10"><path d="M3 1l4 4-4 4" stroke="#8a7b75" fill="none" stroke-width="1.5"/></svg>
      </div>
    </div>
    <div class="tile" role="img" aria-label="Photo of spa towels, stones and green leaves" style="left:260px;background:linear-gradient(135deg,#eef3e4,#a9c48a)"></div>
    <div class="tile" role="img" aria-label="Photo of a back massage treatment" style="left:520px;background:linear-gradient(135deg,#e2c0ae,#8e5e48)"></div>
    <div class="feature" role="img" aria-label="Photo of a woman after a new makeover">
      <div class="cap-top">New Makeover</div>
      <div class="cap-bot">Get the Latest on our<br>Newest Products</div>
    </div>
    <div class="news">
      <div class="news-row"><div class="thumb" role="img" aria-label="Photo of a pedicure"></div><div class="body"><div class="meta"><b>Special manicure and pedicure</b><span>September 20, 2012 · 4 Comments</span></div><p>A soothing soak, gentle scrub and organic oils leave hands and feet soft and renewed for the season ahead.</p></div></div>
      <div class="news-row"><div class="thumb" role="img" aria-label="Photo of a manicure"></div><div class="body"><div class="meta"><b>Special manicure and pedicure</b><span>September 20, 2012 · 4 Comments</span></div><p>A soothing soak, gentle scrub and organic oils leave hands and feet soft and renewed for the season ahead.</p></div></div>
      <div class="news-row"><div class="thumb" role="img" aria-label="Photo of painted nails"></div><div class="body"><div class="meta"><b>Special manicure and pedicure</b><span>September 20, 2012 · 4 Comments</span></div><p>A soothing soak, gentle scrub and organic oils leave hands and feet soft and renewed for the season ahead.</p></div></div>
    </div>
  </div>
</section>

<section class="heart">
  <div class="wrap">
    <div class="heading">
      <span class="kicker">Love it?</span>
      <h2 class="section-title big">HEART IT.</h2>
    </div>
    <div class="cards">
      <div class="card"><div class="img" role="img" aria-label="Photo of feet during a pedicure" style="background:linear-gradient(135deg,#f2dcd0,#c99a84)"></div><div class="price">$100.00</div><div class="icons"><svg width="18" height="16" viewBox="0 0 18 16"><path d="M9 15 2 8a4 4 0 0 1 7-5 4 4 0 0 1 7 5z" fill="#c2185b"/></svg><svg width="18" height="16" viewBox="0 0 18 16"><path d="M9 15 2 8a4 4 0 0 1 7-5 4 4 0 0 1 7 5z" fill="#c2185b"/></svg><svg width="16" height="14"><path d="M1 2h14M1 7h14M1 12h14" stroke="#8a7b75" stroke-width="2"/></svg><svg width="16" height="16"><circle cx="8" cy="8" r="6" stroke="#8a7b75" stroke-width="2" fill="none"/></svg></div></div>
      <div class="card"><div class="img" role="img" aria-label="Photo of a foot soak" style="background:linear-gradient(135deg,#e9c5b3,#8f5c45)"></div><div class="price">$100.00</div><div class="icons"><svg width="18" height="16" viewBox="0 0 18 16"><path d="M9 15 2 8a4 4 0 0 1 7-5 4 4 0 0 1 7 5z" fill="#c2185b"/></svg><svg width="18" height="16" viewBox="0 0 18 16"><path d="M9 15 2 8a4 4 0 0 1 7-5 4 4 0 0 1 7 5z" fill="#c2185b"/></svg><svg width="16" height="14"><path d="M1 2h14M1 7h14M1 12h14" stroke="#8a7b75" stroke-width="2"/></svg><svg width="16" height="16"><circle cx="8" cy="8" r="6" stroke="#8a7b75" stroke-width="2" fill="none"/></svg></div></div>
      <div class="card"><div class="img" role="img" aria-label="Photo of feet with flower petals" style="background:linear-gradient(135deg,#f0d2d6,#b5616f)"></div><div class="price">$100.00</div><div class="icons"><svg width="18" height="16" viewBox="0 0 18 16"><path d="M9 15 2 8a4 4 0 0 1 7-5 4 4 0 0 1 7 5z" fill="#c2185b"/></svg><svg width="18" height="16" viewBox="0 0 18 16"><path d="M9 15 2 8a4 4 0 0 1 7-5 4 4 0 0 1 7 5z" fill="#c2185b"/></svg><svg width="16" height="14"><path d="M1 2h14M1 7h14M1 12h14" stroke="#8a7b75" stroke-width="2"/></svg><svg width="16" height="16"><circle cx="8" cy="8" r="6" stroke="#8a7b75" stroke-width="2" fill="none"/></svg></div></div>
      <div class="card"><div class="img" role="img" aria-label="Photo of red painted toenails" style="background:linear-gradient(135deg,#f3dfd6,#c08a78)"></div><div class="price">$100.00</div><div class="icons"><svg width="18" height="16" viewBox="0 0 18 16"><path d="M9 15 2 8a4 4 0 0 1 7-5 4 4 0 0 1 7 5z" fill="#c2185b"/></svg><svg width="18" height="16" viewBox="0 0 18 16"><path d="M9 15 2 8a4 4 0 0 1 7-5 4 4 0 0 1 7 5z" fill="#c2185b"/></svg><svg width="16" height="14"><path d="M1 2h14M1 7h14M1 12h14" stroke="#8a7b75" stroke-width="2"/></svg><svg width="16" height="16"><circle cx="8" cy="8" r="6" stroke="#8a7b75" stroke-width="2" fill="none"/></svg></div></div>
    </div>
  </div>
</section>

<section class="experts">
  <div class="wrap">
    <div class="heading">
      <span class="kicker">Meet our</span>
      <h2 class="section-title" style="font-size:40px;font-weight:700">EXPERTS AND SPOKESMODELS</h2>
    </div>
    <div class="expert-card">
      <div class="img" role="img" aria-label="Portrait photo of a spokesmodel with a flower in her hair"></div>
      <div class="txt">
        <h4>GO BEHIND<br>THE SCENES</h4>
        <p>Meet the therapists, stylists and faces behind our organic collections. Learn their rituals, favourite products and the secrets they share with every guest who walks through our doors.</p>
        <span class="btn">SEE THEIR STORIES</span>
      </div>
      <svg class="next" width="16" height="26" viewBox="0 0 16 26"><path d="M3 2l10 11L3 24" stroke="#8a7b75" stroke-width="3" fill="none"/></svg>
    </div>
  </div>
</section>

<section class="testi">
  <div class="wrap">
    <div class="heading">
      <h2 class="section-title">What Our Customers Are Saying</h2>
      <span>Dont just take our word for it, take a look at what our customers have to say.</span>
    </div>
    <div class="quote">
      <span class="mark">“</span>
      <p>My monthly visit is the calmest hour of my week. The therapists listen, the products feel pure and my skin has never looked brighter. From the warm welcome to the final cup of tea, every detail feels considered and quietly luxurious. I recommend the signature facial to every friend who asks how I keep my glow through busy seasons and long travel.</p>
      <span class="who">Jade</span>
    </div>
    <div class="faces" role="img" aria-label="Row of customer portrait photos">
      <div></div><div></div><div></div><div class="on"></div><div></div><div></div><div></div><div></div><div></div>
    </div>
  </div>
</section>

<section class="products">
  <div class="wrap">
    <div class="heading">
      <h2 class="section-title">Our Products</h2>
      <span>Nothing but Quality</span>
    </div>
    <div class="tabs"><span class="active">Best Seller</span><span>New Arrivals</span><span>Customer's Choice</span><span>Sale</span></div>
    <div class="tabs-line"></div>
    <div class="shelf">
      <div class="item"><h5>Cooling Gloss</h5><small>NEW · ONLINE ONLY · $22</small><div class="pic" role="img" aria-label="Photo of a red lipstick" style="background:linear-gradient(180deg,#c0203a,#3a1a1a)"></div></div>
      <div class="item"><h5>Makeup Bundle</h5><small>NEW · ONLINE ONLY · $48</small><div class="pic" role="img" aria-label="Photo of a perfume bottle" style="background:linear-gradient(180deg,#f2f2f2,#9aa0a6)"></div></div>
      <div class="item"><h5>Original Perfumes</h5><small>NEW · ONLINE ONLY · $64</small><div class="pic" role="img" aria-label="Photo of a dark perfume box" style="background:linear-gradient(180deg,#5a3a2a,#1c1210)"></div></div>
      <div class="item"><h5>Pocket Book Palette</h5><small>NEW · ONLINE ONLY · $36</small><div class="pic" role="img" aria-label="Photo of an eyeshadow palette" style="background:linear-gradient(180deg,#3a3a3a,#c9a08a)"></div></div>
    </div>
  </div>
</section>

<section class="newsletter">
  <div class="wrap">
    <div class="half">
      <h4>Sign Up for Our Newsletter</h4>
      <div class="signup"><span></span><b>Submit</b></div>
    </div>
    <div class="half">
      <h4>24/7 Customer Service</h4>
      <p>Questions about an order, a booking or your skin? Our team is here any hour of the day to help you choose the right ritual.</p>
    </div>
  </div>
</section>

<footer class="footer">
  <div class="wrap">
    <div class="mag" role="img" aria-label="Magazine cover photo of a model"></div>
    <div class="col" style="left:220px;top:30px;width:330px">
      <h4>eMag</h4>
      <p>Read our seasonal magazine for beauty tips, new arrivals and stories from the salon floor.</p>
    </div>
    <div class="col" style="left:560px;top:30px;width:460px">
      <h4>The Salon</h4>
      <div class="salon-pic" role="img" aria-label="Photo of the salon interior"></div>
      <p>Our salon is a calm retreat in the heart of the city, with private suites, warm light and organic care.</p>
    </div>
    <div class="col hours" style="left:560px;top:190px;width:230px">
      <h4>Opening Time</h4>
      <div><span>Monday - Friday</span><span>9am - 8pm</span></div>
      <div><span>Saturday</span><span>9am - 6pm</span></div>
      <div><span>Sunday</span><span>10am - 4pm</span></div>
      <div><span>Holidays</span><span>Closed</span></div>
    </div>
    <div class="col contact" style="left:820px;top:190px;width:220px">
      <h4>Contact Us</h4>
      <p>12 Rosewater Lane, Suite 4</p>
      <p>Fairview, CA 90000</p>
      <p>+1 (555) 014-2290</p>
      <p>hello@velunabay.example</p>
    </div>
  </div>
</footer>

<div class="bottom">
  <div class="wrap">
    <div class="pay"><i></i><i></i><i></i><i></i></div>
    <span class="copy">© 2013 · VelunaBay · All Rights Reserved</span>
  </div>
</div>

</body>
</html>
```